App Design for quiz app (casual gaming app)

We need an design & logo for our quiz app. Its a simple quiz app, where you pick up a category, answer three questions out of this category. After this an opponent is assigned to your game, and has to answer the same three questions. After this first round is finished, it's the opponents turn to choose a new category and answer three questions out of this category. Now it's your turn to answer the same three questions. With this done, the 2nd round is finished. One game has seven rounds.
Please find attached the balsamiq project. For all of you, do not have balsamiq, please find also the mockups as pdf.
Final delivery should be psd files
Target Market(s)
Casual Games

```html
<!DOCTYPE html>
<html lang="en">
<head>
<meta charset="utf-8">
<title>Quiz App – Side Menu</title>
<link href="https://fonts.googleapis.com/css2?family=Hind:wght@300;400;500&display=swap" rel="stylesheet">
<style>
  :root {
    --backdrop: #5f8dab;
    --status-green: #1fbd5c;
    --drawer: #2a2e45;
    --menu-text: #c3c7d6;
    --icon-stroke: #8e94ab;
    --name-text: #ffffff;
    --content-white: #f7f8f8;
    --row-mint: #e4f3ea;
    --divider-green: #3fbf74;
    --button-green: #22b45a;
    --photo-warm: #d9b08f;
    --photo-rose: #c58c84;
    --photo-cool: #b9c3cf;
    --photo-amber: #c98a4a;
  }
  * { box-sizing: border-box; margin: 0; padding: 0; }
  html, body { width: 1200px; height: 900px; overflow: hidden; }
  body {
    background: var(--backdrop);
    font-family: "Hind", "Helvetica Neue", Arial, sans-serif;
  }
  .screen {
    position: absolute;
    left: 390px; top: 77px;
    width: 420px; height: 746px;
    overflow: hidden;
    background: var(--drawer);
    box-shadow: 0 20px 50px rgba(20, 40, 60, .35);
  }
  .status-bar {
    position: absolute; left: 0; top: 0; width: 100%; height: 22px;
    background: var(--status-green);
    color: #fff; font-size: 12px; font-weight: 500;
    display: flex; align-items: center; justify-content: space-between;
    padding: 0 8px;
  }
  .status-bar .carrier, .status-bar .battery { display: flex; align-items: center; gap: 5px; }
  .status-bar .time { position: absolute; left: 50%; transform: translateX(-50%); }

  /* content peeking behind the drawer */
  .content {
    position: absolute; left: 336px; top: 22px; right: 0; bottom: 0;
    background: var(--row-mint);
  }
  .content .header-area {
    position: absolute; left: 0; top: 0; width: 100%; height: 160px;
    background: var(--content-white);
  }
  .content .header-photo {
    position: absolute; left: -40px; top: 40px; width: 84px; height: 84px;
    border-radius: 50%;
    background: radial-gradient(circle at 40% 40%, #efd8bf, var(--photo-warm));
  }
  .content .add-button {
    position: absolute; left: -20px; top: 168px; width: 80px; height: 44px;
    background: var(--button-green); color: #fff;
    font-size: 24px; font-weight: 300;
    display: flex; align-items: center; justify-content: center;
  }
  .content .row {
    position: absolute; left: 0; width: 100%; height: 112px;
    border-top: 1px solid var(--divider-green);
  }
  .content .row-photo {
    position: absolute; left: 14px; top: 22px; width: 68px; height: 68px; border-radius: 50%;
  }

  .drawer { position: absolute; left: 0; top: 22px; width: 336px; bottom: 0; background: var(--drawer); }
  .profile { position: absolute; left: 38px; top: 44px; display: flex; align-items: center; gap: 22px; }
  .profile .avatar {
    width: 54px; height: 54px; border-radius: 50%;
    background: radial-gradient(circle at 45% 40%, #f1dcc4, var(--photo-warm));
    border: 2px solid #e9e3dc;
  }
  .profile .name { color: var(--name-text); font-size: 20px; font-weight: 400; }

  .menu { position: absolute; left: 40px; top: 168px; list-style: none; }
  .menu li {
    display: flex; align-items: center; height: 66px;
    color: var(--menu-text); font-size: 17px; font-weight: 400; letter-spacing: .2px;
  }
  .menu svg, .sign-out svg { width: 30px; height: 30px; margin-right: 24px; fill: none; stroke: var(--icon-stroke); stroke-width: 1.4; stroke-linecap: round; stroke-linejoin: round; }
  .sign-out {
    position: absolute; left: 40px; bottom: 36px;
    display: flex; align-items: center;
    color: var(--menu-text); font-size: 18px; font-weight: 400;
  }
</style>
</head>
<body>
  <div class="screen">
    <div class="status-bar">
      <span class="carrier">
        <svg width="34" height="8" viewBox="0 0 34 8"><g fill="#fff"><circle cx="4" cy="4" r="3"/><circle cx="11" cy="4" r="3"/><circle cx="18" cy="4" r="3"/></g><g fill="none" stroke="#fff"><circle cx="25" cy="4" r="2.6"/><circle cx="31" cy="4" r="2.6"/></g></svg>
        ABC
        <svg width="14" height="10" viewBox="0 0 14 10" fill="none" stroke="#fff" stroke-width="1.4"><path d="M1 3.5a8.5 8.5 0 0 1 12 0"/><path d="M3.3 5.8a5 5 0 0 1 7.4 0"/><circle cx="7" cy="8.4" r=".9" fill="#fff"/></svg>
      </span>
      <span class="time">4:21 PM</span>
      <span class="battery">
        <svg width="7" height="11" viewBox="0 0 7 11" fill="none" stroke="#fff" stroke-width="1"><path d="M1 3l5 5-2.5 2.5V.5L6 3 1 8"/></svg>
        22%
        <svg width="24" height="11" viewBox="0 0 24 11"><rect x=".5" y=".5" width="20" height="10" rx="2" fill="none" stroke="#fff"/><rect x="2" y="2" width="4.5" height="7" fill="#fff"/><rect x="21.5" y="3.5" width="2" height="4" fill="#fff"/></svg>
      </span>
    </div>

    <div class="content">
      <div class="header-area">
        <div class="header-photo" role="img" aria-label="Profile photo of the current player"></div>
      </div>
      <div class="add-button">+</div>
      <div class="row" style="top:222px">
        <div class="row-photo" role="img" aria-label="Opponent profile photo" style="background:radial-gradient(circle at 45% 40%, #ead0c2, var(--photo-rose))"></div>
      </div>
      <div class="row" style="top:334px">
        <div class="row-photo" role="img" aria-label="Opponent profile photo" style="background:radial-gradient(circle at 45% 40%, #eef0f2, var(--photo-cool))"></div>
      </div>
      <div class="row" style="top:446px">
        <div class="row-photo" role="img" aria-label="Opponent profile photo" style="background:radial-gradient(circle at 45% 40%, #efc9a0, var(--photo-amber))"></div>
      </div>
    </div>

    <nav class="drawer">
      <div class="profile">
        <div class="avatar" role="img" aria-label="Profile photo of Mara Lenz"></div>
        <span class="name">Mara Lenz</span>
      </div>

      <ul class="menu">
        <li>
          <svg viewBox="0 0 30 30"><path d="M4 7v17"/><path d="M7 6v19"/><path d="M10 5h10l5 5v16H10z"/><path d="M20 5v5h5"/></svg>
          Overview
        </li>
        <li>
          <svg viewBox="0 0 30 30"><path d="M3 7h15v10H9l-4 3v-3H3z"/><path d="M18 11h9v10h-2v3l-4-3h-8v-4"/></svg>
          My Groups
        </li>
        <li>
          <svg viewBox="0 0 30 30"><circle cx="11" cy="10" r="4.5"/><path d="M3 25v-3a6 6 0 0 1 6-6h4a6 6 0 0 1 6 6v3z"/><circle cx="20" cy="9" r="4"/><path d="M21 15h1a6 6 0 0 1 6 6v3h-6"/></svg>
          Invite Friends
        </li>
        <li>
          <svg viewBox="0 0 30 30"><path d="M3 4v23h24"/><path d="M8 26v-7M12 26v-10M16 26v-6M20 26v-11M24 26v-14"/><path d="M7 16l6-6 4 3 8-8"/><path d="M21 5h4v4"/></svg>
          Stats
        </li>
        <li>
          <svg viewBox="0 0 30 30"><circle cx="15" cy="15" r="12"/><path d="M11.5 12a3.5 3.5 0 1 1 5 3.2c-1 .5-1.5 1.2-1.5 2.3v.8"/><circle cx="15" cy="21.5" r=".6" fill="#8e94ab"/></svg>
          Help
        </li>
        <li>
          <svg viewBox="0 0 30 30"><path d="M3 11l12-5 12 5-12 5z"/><path d="M3 15l12 5 12-5"/><path d="M3 19l12 5 12-5"/><path d="M3 11v8M27 11v8"/></svg>
          Imprints
        </li>
      </ul>

      <div class="sign-out">
        <svg viewBox="0 0 30 30"><path d="M12 4h14v22H12v-5"/><path d="M12 9V4"/><path d="M18 15H4"/><path d="M8 11l-4 4 4 4"/></svg>
        Sign Out
      </div>
    </nav>
  </div>
</body>
</html>
```